!st birthday celebration

Im looking for a celebration type of flyer for our first birthday. something colorful and eye catching but with a vintage feel to it. we are a vintage shop with a friendly atmosphere and always have music playing. I have attached a draft copy i have been working on so far. Thanks

Industry/Entity Type

Shop

```html
<!DOCTYPE html>
<html lang="en">
<head>
<meta charset="utf-8">
<title>Marlow Vintage – 1st Birthday</title>
<link rel="stylesheet" href="https://fonts.googleapis.com/css2?family=Libre+Bodoni:wght@400;700&family=Vollkorn:wght@400;700&family=Source+Serif+4:wght@700&display=swap">
<style>
  :root {
    --ink: #1c1a17;
    --frame: #231f1c;
    --stripe-red: #e2461f;
    --stripe-gold: #f7b43c;
    --cream: #fbe98a;
    --plaque: #f4d14a;
    --ribbon-text: #f6d46a;
    --glow: #fff6a8;
    --footer-text: #ffffff;
  }
  * { box-sizing: border-box; margin: 0; padding: 0; }
  html, body { width: 849px; height: 1200px; overflow: hidden; background: var(--frame); }

  .flyer {
    position: relative;
    width: 849px;
    height: 1200px;
    background: var(--frame);
    font-family: "Vollkorn", Georgia, serif;
    color: var(--ink);
  }

  .poster {
    position: absolute;
    left: 18px; top: 12px;
    width: 813px; height: 1122px;
    border-radius: 34px;
    overflow: hidden;
    background:
      repeating-linear-gradient(90deg,
        var(--stripe-gold) 0 62px,
        var(--stripe-red) 62px 132px);
  }
  .poster::before {
    content: "";
    position: absolute; inset: 0;
    background: radial-gradient(ellipse 60% 32% at 50% 46%, rgba(255,246,168,.95) 0%, rgba(255,230,120,.7) 45%, rgba(255,210,90,0) 100%);
  }
  .poster::after {
    content: "";
    position: absolute; inset: 0;
    border: 10px solid var(--cream);
    border-radius: 34px;
    opacity: .75;
  }

  .photo-area {
    position: absolute;
    left: 60px; top: 610px;
    width: 700px; height: 480px;
    border-radius: 20px;
    background: radial-gradient(ellipse at 40% 60%, rgba(255,235,130,.85), rgba(238,120,40,.65) 60%, rgba(226,70,31,.25) 100%);
  }

  .plaque {
    position: absolute;
    left: 70px; top: 45px;
    width: 710px; height: 170px;
    background: var(--plaque);
    border: 6px solid var(--ink);
    border-radius: 26px;
    box-shadow: inset 0 0 0 5px var(--cream);
    display: flex; align-items: center; justify-content: center;
  }
  .brand-name {
    font-family: "Libre Bodoni", Georgia, serif;
    font-weight: 700;
    font-size: 76px;
    color: var(--ink);
  }

  .ribbon {
    position: absolute;
    left: 105px; top: 288px;
    width: 640px; height: 60px;
  }
  .ribbon svg { position: absolute; inset: 0; }
  .ribbon-text {
    position: absolute; inset: 0;
    display: flex; align-items: center; justify-content: center;
    font-family: "Libre Bodoni", Georgia, serif;
    font-size: 19px;
    letter-spacing: .5px;
    color: var(--ribbon-text);
  }

  .headline {
    position: absolute;
    left: 0; right: 0; top: 362px;
    text-align: center;
    font-family: "Libre Bodoni", Georgia, serif;
    font-weight: 400;
    color: var(--ink);
    text-shadow: 0 0 18px var(--glow), 0 0 8px var(--glow);
  }
  .headline .line-lg { display: block; font-size: 84px; line-height: 96px; }
  .headline .line-md { display: block; font-size: 50px; line-height: 70px; }

  .details {
    position: absolute;
    left: 0; right: 0; top: 644px;
    text-align: center;
    font-size: 24px;
    line-height: 49px;
    text-shadow: 0 0 10px var(--glow);
  }

  .festivities {
    position: absolute;
    left: 0; right: 0; top: 836px;
    text-align: center;
    font-size: 17px;
    line-height: 27.5px;
    text-shadow: 0 0 8px var(--glow);
    list-style: none;
  }
  .festivities li::before { content: "•  "; }
  .festivities .intro::before { content: none; }

  .footer {
    position: absolute;
    left: 0; right: 0; top: 1142px; height: 58px;
    display: flex; align-items: center; justify-content: center;
    gap: 14px;
    font-family: "Source Serif 4", Georgia, serif;
    font-weight: 700;
    font-size: 14.5px;
    letter-spacing: .6px;
    color: var(--footer-text);
  }
</style>
</head>
<body>
<main class="flyer">
  <section class="poster">
    <div class="photo-area" role="img" aria-label="Warm-toned photo of a vintage car parked outside the shop"></div>

    <header class="plaque">
      <span class="brand-name">Marlow Vintage</span>
    </header>

    <div class="ribbon">
      <svg width="640" height="60" viewBox="0 0 640 60" aria-hidden="true">
        <polygon points="0,0 640,0 622,30 640,60 0,60 18,30" fill="#1c1a17"/>
      </svg>
      <div class="ribbon-text">VINTAGE - RETRO CLOTHING &amp; COLLECTABLES</div>
    </div>

    <h1 class="headline">
      <span class="line-lg">HAPPY 1ST</span>
      <span class="line-lg">BIRTHDAY</span>
      <span class="line-md">MARLOW VINTAGE!</span>
    </h1>

    <div class="details">
      <p>You are invited to help celebrate in the festivities!</p>
      <p>Date: 19th &amp; 20th July</p>
      <p>From 11:00am onwards</p>
    </div>

    <ul class="festivities">
      <li class="intro">Festivities will include:</li>
      <li>pop up market stalls,</li>
      <li>best dressed vintage outfit,</li>
      <li>face painting</li>
      <li>vintage cars on display</li>
      <li>music</li>
      <li>refreshments</li>
    </ul>
  </section>

  <footer class="footer">
    <span>88 HARBOUR VIEW RD, ELMSTEAD</span><span>|</span>
    <span>PHONE: 5900 1234</span><span>|</span>
    <span>MOBILE: 0400000111</span>
  </footer>
</main>
</body>
</html>
```